A new type of air filter for interior of vehicles

HI
I have included a file to show the basics of what i want and all the information that should be needed ,i now need this to be "designed" and to be created for a information flyer first and as things progress web pages etc etc look forward to the designs

Industry/Entity Type

Interior

Contact Information for Business Card

probably the same "theme type" as the brochure which will carry through to Business card and on to online marketing in the future

Font styles to use
Serif
Sans Serif

```html
<!DOCTYPE html>
<html lang="en">
<head>
<meta charset="utf-8">
<title>Clearway Cabin Filters – Information Flyer</title>
<link rel="stylesheet" href="https://fonts.googleapis.com/css2?family=Exo+2:ital,wght@0,400;0,600;0,700;1,500;1,700;1,800&display=swap">
<style>
  :root {
    --brand-red: #dc1f47;
    --brand-red-dark: #b5163a;
    --ink: #2b2b2b;
    --bar-dark: #262626;
    --panel-top: #fafafa;
    --panel-bottom: #e3e3e3;
    --sky-top: #3f7fc4;
    --sky-bottom: #cfe3f5;
    --page-bg: #ececec;
    --white: #ffffff;
  }
  * { margin: 0; padding: 0; box-sizing: border-box; }
  html, body {
    width: 1000px; height: 1200px; overflow: hidden;
    background: var(--page-bg);
    font-family: "Exo 2", sans-serif;
    color: var(--ink);
  }
  .flyer {
    position: absolute; left: 102px; top: 37px;
    width: 796px; height: 1123px;
    background: var(--white);
    box-shadow: 0 4px 14px rgba(0,0,0,.25);
    overflow: hidden;
  }
  /* Header */
  .masthead { position: absolute; left: 0; top: 0; width: 796px; height: 158px; background: var(--brand-red); }
  .masthead-art { position: absolute; inset: 0; }
  .brand-title {
    position: absolute; left: 38px; top: 36px;
    font-weight: 800; font-style: italic; font-size: 41px; line-height: 46px;
    color: var(--white); letter-spacing: -0.3px;
  }
  .contact-bar {
    position: absolute; left: 0; top: 158px; width: 796px; height: 33px;
    background: linear-gradient(#3a3a3a, var(--bar-dark));
    color: var(--white); font-style: italic; font-weight: 500; font-size: 16px;
  }
  .contact-bar .item { position: absolute; top: 7px; display: flex; align-items: center; gap: 7px; }
  .contact-bar .web { left: 40px; }
  .contact-bar .mail { right: 38px; }
  /* Intro panel */
  .intro-panel {
    position: absolute; left: 0; top: 191px; width: 796px; height: 392px;
    background: linear-gradient(var(--panel-top), var(--panel-bottom));
  }
  .zigzag { position: absolute; left: 0; top: 568px; width: 796px; height: 16px; }
  .photo-frame {
    position: absolute; left: 38px; width: 230px; height: 156px;
    background: var(--white); padding: 5px;
    box-shadow: 0 6px 8px rgba(0,0,0,.22);
  }
  .photo-frame .fill { width: 100%; height: 100%; }
  .photo-vent { top: 209px; }
  .photo-vent .fill { background: linear-gradient(135deg, #5a5d62, #2f3135 60%, #8b8e93); }
  .photo-exhaust { top: 391px; }
  .photo-exhaust .fill { background: linear-gradient(90deg, #e9e9e6 0%, #b9c3cc 45%, #3f74b8 100%); }
  .block { position: absolute; }
  .block h2 {
    color: var(--brand-red); font-style: italic; font-weight: 700;
    font-size: 21px; line-height: 26px; margin-bottom: 6px;
  }
  .block p { font-size: 14.6px; line-height: 16.1px; text-align: justify; }
  .block-what { left: 288px; top: 221px; width: 470px; }
  .block-why { left: 288px; top: 384px; width: 470px; }
  .block-how { left: 205px; top: 601px; width: 554px; }
  .block-diff { left: 268px; top: 835px; width: 490px; }
  .block-how p, .block-diff p { font-size: 15.2px; line-height: 21.5px; }
  /* Product imagery */
  .product-filter { position: absolute; left: 20px; top: 600px; width: 190px; height: 315px; }
  .product-detail {
    position: absolute; left: 108px; top: 890px; width: 134px; height: 134px;
    border-radius: 50%; border: 4px solid var(--brand-red);
    background: radial-gradient(circle at 40% 50%, #4a4a4a, #1c1c1c 45%, #d9d9d9 75%);
  }
  .product-arrow { position: absolute; left: 30px; top: 880px; width: 90px; height: 100px; }
  /* Footer */
  .footer {
    position: absolute; left: 0; top: 1055px; width: 796px; height: 68px;
    background: var(--brand-red); color: var(--white);
  }
  .footer .address { position: absolute; left: 38px; top: 10px; font-weight: 600; font-size: 14.5px; line-height: 16.5px; }
  .footer .call { position: absolute; right: 46px; top: 15px; font-style: italic; font-weight: 500; font-size: 22px; }
  .footer .call strong { font-weight: 800; font-size: 27px; letter-spacing: 0.3px; }
</style>
</head>
<body>
<main class="flyer">

  <header class="masthead">
    <svg class="masthead-art" viewBox="0 0 796 158" width="796" height="158">
      <defs>
        <linearGradient id="sky" x1="0" y1="0" x2="0" y2="1">
          <stop offset="0" stop-color="#3f7fc4"/>
          <stop offset="1" stop-color="#cfe3f5"/>
        </linearGradient>
      </defs>
      <polygon points="468,0 480,0 434,158 422,158" fill="#ffffff"/>
      <polygon points="480,0 796,0 796,158 434,158" fill="url(#sky)" role="img" aria-label="Bright sky with clouds and large metallic lettering"/>
    </svg>
    <h1 class="brand-title">CLEARWAY CABIN<br>FILTERS</h1>
  </header>

  <div class="contact-bar">
    <div class="item web">
      <svg width="18" height="18" viewBox="0 0 18 18"><circle cx="9" cy="9" r="7.5" fill="none" stroke="#fff" stroke-width="1.6"/><path d="M1.5 9h15M9 1.5c-3 3-3 12 0 15M9 1.5c3 3 3 12 0 15" fill="none" stroke="#fff" stroke-width="1.2"/></svg>
      <span>ClearwayCabinFilters.com.au</span>
    </div>
    <div class="item mail">
      <svg width="22" height="15" viewBox="0 0 22 15"><rect x="1" y="1" width="20" height="13" fill="none" stroke="#fff" stroke-width="1.8"/><path d="M1 1l10 8 10-8" fill="none" stroke="#fff" stroke-width="1.8"/></svg>
      <span>hello@clearwaycabin.com.au</span>
    </div>
  </div>

  <section class="intro-panel"></section>
  <svg class="zigzag" viewBox="0 0 796 16" width="796" height="16" preserveAspectRatio="none">
    <path d="M0 0 H796 V15 L787 4 L778 15 L769 4 L760 15 L751 4 L742 15 L733 4 L724 15 L715 4 L706 15 L697 4 L688 15 L679 4 L670 15 L661 4 L652 15 L643 4 L634 15 L625 4 L616 15 L607 4 L598 15 L589 4 L580 15 L571 4 L562 15 L553 4 L544 15 L535 4 L526 15 L517 4 L508 15 L499 4 L490 15 L481 4 L472 15 L463 4 L454 15 L445 4 L436 15 L427 4 L418 15 L409 4 L400 15 L391 4 L382 15 L373 4 L364 15 L355 4 L346 15 L337 4 L328 15 L319 4 L310 15 L301 4 L292 15 L283 4 L274 15 L265 4 L256 15 L247 4 L238 15 L229 4 L220 15 L211 4 L202 15 L193 4 L184 15 L175 4 L166 15 L157 4 L148 15 L139 4 L130 15 L121 4 L112 15 L103 4 L94 15 L85 4 L76 15 L67 4 L58 15 L49 4 L40 15 L31 4 L22 15 L13 4 L4 15 L0 10 Z" fill="#e3e3e3"/>
  </svg>

  <figure class="photo-frame photo-vent"><div class="fill" role="img" aria-label="Car dashboard air vent with air flowing out"></div></figure>
  <figure class="photo-frame photo-exhaust"><div class="fill" role="img" aria-label="Vehicle exhaust pipe releasing a cloud of fumes"></div></figure>

  <article class="block block-what">
    <h2>What is a Cabin Air Filter ?</h2>
    <p>Cabin air filters with dual layer carbon activated filter media, are designed to remove nearly 100% of airborn particles, like pollen, road dust, soot and other microscopic particles. The activated carbon also helps to remove over 80% of noxious fumes emitting from your vehicles air vents.</p>
  </article>

  <article class="block block-why">
    <h2>Why is a Cabin Air Filter important ?</h2>
    <p>Surrounding traffic creates poisonous gases and heavy metal pollutants that are directed straight into your vehicles interior. Apart the obvious health concerns unfiltered air can lead to allergies, asthma and other respiratory problems. With over 4 million Australians suffering from allergies, our activated carbon cabin filter are an essential part of your vehicles ventilation system.</p>
  </article>

  <div class="product-filter" role="img" aria-label="Red framed cabin filter panel with black carbon foam media">
    <svg viewBox="0 0 190 315" width="190" height="315">
      <defs>
        <linearGradient id="filterFill" x1="0" y1="0" x2="1" y2="1">
          <stop offset="0" stop-color="#2a2a2a"/>
          <stop offset="1" stop-color="#111"/>
        </linearGradient>
      </defs>
      <polygon points="6,8 178,40 178,312 6,296" fill="#c81d3f"/>
      <polygon points="18,22 170,50 170,300 18,286" fill="url(#filterFill)"/>
    </svg>
  </div>
  <svg class="product-arrow" viewBox="0 0 90 100" width="90" height="100">
    <path d="M6 4 C10 50 40 80 78 88" fill="none" stroke="#dc1f47" stroke-width="1.5"/>
    <path d="M70 82 L80 88 L70 93" fill="none" stroke="#dc1f47" stroke-width="1.5"/>
  </svg>
  <div class="product-detail" role="img" aria-label="Close-up of the carbon foam filter layer inside the red frame"></div>

  <article class="block block-how">
    <h2>How do Cabin Air Filters work ?</h2>
    <p>Our Cabin Air Filters work by filtering the outside air entering your vehicle. Clearway Cabin Filters' unique design has a first layer of sponge like material, coated in a layer of activated carbon(each gram has the same surface area as a football field) this layer traps larger particles and helps absorb odours while maintaining the maximum surface filtering area . The second layer of fine spun micro fibre also coated in activated carbon helps trap dangerous smaller microscopic particles and provides an extra layer of absorption while still maintaining maximum air flow.</p>
  </article>

  <article class="block block-diff">
    <h2>Why is Clearway Cabin Filters Different ?</h2>
    <p>Our Cabin Filters are a complete new Australian design. By greatly increasing the surface area in contact with incoming air, over conventional type "pleated filters" we are able to maintain high air flow while greatly increasing filtering capacity, with the added benefit of activated carbon coating in contact with all areas of air flow. All our filter support bases are low allergy, cast acylic, laser cut to suit individual vehicles,and our activated carbon is sourced from coconut shells Our 2 stages of filter media is of the highest quality available.</p>
  </article>

  <footer class="footer">
    <p class="address">PO BOX 48<br>Harbour Bend Qld<br>4999</p>
    <p class="call">Call Us Now ! <strong>0400 555 018</strong></p>
  </footer>

</main>
</body>
</html>
```